Visitenkarte erstellen für Reiki Praxis

Visitenkarten für Reiki Praxis Doppelseitig

business cards reiki practice double-sided

The background can also be a different color

```html
<!DOCTYPE html>
<html lang="en">
<head>
<meta charset="utf-8">
<title>Quiet Current – Business Card</title>
<link rel="stylesheet" href="https://fonts.googleapis.com/css2?family=Open+Sans:wght@400;600;700&display=swap">
<style>
  :root {
    --page-bg: #1a1a1a;
    --card-bg: #141414;
    --card-edge: #0b0b0b;
    --pattern-a: #1d1b1c;
    --pattern-b: #232021;
    --gold: #e9a825;
    --white: #f4f1ec;
    --rose: #c9a3a8;
    --soft: #d8d4cf;
  }
  html, body {
    margin: 0;
    padding: 0;
    width: 1200px;
    height: 900px;
    overflow: hidden;
    background: var(--page-bg);
    font-family: "Open Sans", Arial, sans-serif;
  }
  .canvas {
    position: relative;
    width: 1200px;
    height: 900px;
  }
  .card {
    position: absolute;
    left: 280px;
    width: 640px;
    height: 366px;
    border-radius: 18px;
    background: var(--card-bg);
    box-shadow: 0 3px 0 var(--card-edge), 0 18px 40px rgba(0,0,0,0.55);
    overflow: hidden;
  }
  .card--back { top: 60px; }
  .card--front { top: 474px; }

  .back-pattern {
    position: absolute;
    inset: 0;
    background: linear-gradient(135deg, var(--pattern-a), var(--pattern-b) 55%, var(--pattern-a));
  }
  .back-mark {
    position: absolute;
    right: 72px;
    top: 150px;
    display: flex;
    align-items: center;
    gap: 8px;
    font-size: 12px;
    font-weight: 600;
    letter-spacing: 1.5px;
    color: var(--rose);
    text-transform: uppercase;
  }
  .back-mark .dot {
    width: 10px; height: 10px; border-radius: 50%;
    background: var(--rose);
  }

  .brand {
    position: absolute;
    left: 44px;
    top: 92px;
  }
  .brand__name {
    display: flex;
    align-items: center;
    gap: 10px;
    font-size: 25px;
    font-weight: 400;
    letter-spacing: 1.5px;
    color: var(--white);
    text-transform: uppercase;
  }
  .brand__name .dot {
    width: 12px; height: 12px; border-radius: 50%;
    background: var(--rose);
  }
  .brand__owner {
    margin: 4px 0 0 70px;
    font-size: 16px;
    letter-spacing: 5px;
    color: var(--gold);
    text-transform: uppercase;
  }

  .divider {
    position: absolute;
    left: 72px;
    right: 40px;
    top: 200px;
    height: 1px;
    background: linear-gradient(90deg, var(--rose), var(--gold));
  }

  .person {
    position: absolute;
    right: 46px;
    top: 142px;
    text-align: right;
  }
  .person__name {
    font-size: 21px;
    font-weight: 700;
    color: var(--gold);
    text-transform: uppercase;
    line-height: 1.1;
  }
  .person__role {
    font-size: 14px;
    color: var(--white);
  }

  .address {
    position: absolute;
    right: 46px;
    top: 222px;
    text-align: right;
    font-size: 14px;
    line-height: 1.45;
    color: var(--white);
  }

  .contact {
    position: absolute;
    left: 72px;
    top: 222px;
    list-style: none;
    margin: 0;
    padding: 0;
    font-size: 16px;
    line-height: 1.6;
    color: var(--white);
  }
  .contact li {
    display: flex;
    align-items: center;
    gap: 8px;
  }
  .contact svg {
    width: 14px;
    height: 14px;
    fill: var(--gold);
    flex: none;
  }
</style>
</head>
<body>
<main class="canvas">

  <section class="card card--back" aria-label="Card back">
    <div class="back-pattern" role="img" aria-label="Tone-on-tone repeating floral pattern across the card back"></div>
    <div class="back-mark"><span class="dot"></span>Quiet Current</div>
  </section>

  <section class="card card--front" aria-label="Card front">
    <div class="brand">
      <div class="brand__name"><span class="dot"></span>Quiet Current</div>
      <div class="brand__owner">Mara Lind</div>
    </div>

    <div class="person">
      <div class="person__name">Nora Hale</div>
      <div class="person__role">Founder/CEO</div>
    </div>

    <div class="divider"></div>

    <ul class="contact">
      <li>
        <svg viewBox="0 0 16 16" aria-hidden="true"><path d="M3.6 1.5l2.3 2.8-1.3 1.6c.9 2 2.6 3.7 4.6 4.6l1.6-1.3 2.8 2.3-1.5 2.2C6.8 13.3 2.7 9.2 1.4 3z"/></svg>
        (555) 201 3384
      </li>
      <li>
        <svg viewBox="0 0 16 16" aria-hidden="true"><path d="M1 3h14v10H1z M2 4l6 5 6-5" fill="none" stroke="#e9a825" stroke-width="1.6"/></svg>
        info@quietcurrent.com
      </li>
      <li>
        <svg viewBox="0 0 16 16" aria-hidden="true"><circle cx="8" cy="8" r="6.5" fill="none" stroke="#e9a825" stroke-width="1.5"/><path d="M1.5 8h13M8 1.5c-3 3.5-3 9.5 0 13M8 1.5c3 3.5 3 9.5 0 13" fill="none" stroke="#e9a825" stroke-width="1.2"/></svg>
        www.quietcurrent.com
      </li>
    </ul>

    <div class="address">
      812 Linden Row<br>
      Westfield AB 30215
    </div>
  </section>

</main>
</body>
</html>
```